Accounting business needs business card

I have a business card but need something better. I want the colour changed and the design to be better. I have uploaded a picture of my new sign that is grey in colour, i would like to incorporate these colours.

```html
<!DOCTYPE html>
<html lang="en">
<head>
<meta charset="utf-8">
<title>Kestrel Tax – Business Card</title>
<link rel="stylesheet" href="https://fonts.googleapis.com/css2?family=Montserrat:wght@400;500;600;700&family=Tinos&display=swap">
<style>
  :root {
    --backdrop: #e4e6e8;
    --ink: #2b2d30;
    --ink-soft: #6f7378;
    --silver-light: #fbfbfb;
    --silver-mid: #e3e4e6;
    --silver-dark: #c9cacc;
    --steel-light: #d6d7d9;
    --steel-mid: #bdbec0;
    --steel-dark: #a6a7a9;
    --badge-fill: #9a9ca0;
    --badge-fill-light: #b9bbbe;
  }
  * { margin: 0; padding: 0; box-sizing: border-box; }
  html, body { width: 1200px; height: 913px; overflow: hidden; }
  body {
    background: var(--backdrop);
    font-family: "Montserrat", sans-serif;
    color: var(--ink);
    position: relative;
  }
  .card {
    position: absolute;
    width: 560px;
    height: 320px;
    border-radius: 4px;
    box-shadow: 0 10px 24px rgba(0,0,0,.18);
    overflow: hidden;
  }
  .card--front {
    left: 60px; top: 60px;
    background:
      repeating-linear-gradient(0deg, rgba(255,255,255,.18) 0 1px, rgba(0,0,0,.02) 1px 3px),
      linear-gradient(160deg, var(--silver-dark) 0%, var(--silver-light) 45%, var(--silver-mid) 100%);
  }
  .card--back {
    left: 580px; top: 533px;
    background:
      repeating-linear-gradient(0deg, rgba(255,255,255,.12) 0 1px, rgba(0,0,0,.03) 1px 3px),
      linear-gradient(160deg, var(--steel-dark) 0%, var(--steel-light) 50%, var(--steel-mid) 100%);
  }

  .brand {
    position: absolute;
    display: flex;
    flex-direction: column;
    align-items: center;
  }
  .brand__mark {
    border: 2.5px solid var(--ink);
    border-radius: 50%;
  }
  .brand__name {
    font-weight: 500;
    color: var(--ink);
    white-space: nowrap;
  }
  .card--front .brand { left: 250px; top: 22px; width: 260px; }
  .card--front .brand__mark { width: 76px; height: 76px; }
  .card--front .brand__name { font-size: 21px; letter-spacing: 11px; margin-right: -11px; margin-top: 14px; }

  .card--back .brand { left: 0; right: 0; top: 62px; }
  .card--back .brand__mark { width: 112px; height: 112px; border-width: 3px; }
  .card--back .brand__name { font-size: 34px; letter-spacing: 18px; margin-right: -18px; margin-top: 24px; font-weight: 600; }

  .person {
    position: absolute;
    left: 36px; top: 160px;
  }
  .person__name { font-size: 22px; font-weight: 700; letter-spacing: .3px; }
  .person__credentials,
  .person__role { font-size: 12px; color: var(--ink-soft); margin-top: 4px; letter-spacing: .4px; }

  .contact {
    position: absolute;
    left: 36px; bottom: 22px;
    list-style: none;
  }
  .contact__item {
    display: flex; align-items: center;
    font-size: 13px; letter-spacing: .4px;
    color: var(--ink);
    margin-top: 5px;
  }
  .contact__icon { width: 14px; height: 14px; margin-right: 12px; fill: var(--ink); }

  .affiliations {
    position: absolute;
    right: 28px; bottom: 30px;
    display: flex; align-items: center; gap: 10px;
  }
  .affiliations__badge {
    width: 96px; height: 30px;
    background: var(--badge-fill);
  }
  .affiliations__note {
    font-family: "Tinos", serif;
    font-size: 8px; line-height: 1.15; color: var(--ink);
  }
  .affiliations__partner {
    width: 40px; height: 40px; border-radius: 50%;
    background: var(--badge-fill-light);
    margin-left: 4px; align-self: flex-start; margin-top: -36px;
  }
</style>
</head>
<body>

<section class="card card--front" aria-label="Card front">
  <div class="brand">
    <div class="brand__mark"></div>
    <div class="brand__name">KESTREL TAX</div>
  </div>

  <div class="person">
    <h1 class="person__name">Liam Hartwell</h1>
    <p class="person__credentials">CPA, MTAX, BCOM (Acc &amp; Fin)</p>
    <p class="person__role">Taxation and Business Accountant</p>
  </div>

  <ul class="contact">
    <li class="contact__item">
      <svg class="contact__icon" viewBox="0 0 24 24" aria-hidden="true"><path d="M6.6 10.8a15 15 0 0 0 6.6 6.6l2.2-2.2a1 1 0 0 1 1-.25 11.4 11.4 0 0 0 3.6.57 1 1 0 0 1 1 1V20a1 1 0 0 1-1 1A17 17 0 0 1 3 4a1 1 0 0 1 1-1h3.5a1 1 0 0 1 1 1c0 1.25.2 2.45.57 3.6a1 1 0 0 1-.25 1z"/></svg>
      0412 555 018
    </li>
    <li class="contact__item">
      <svg class="contact__icon" viewBox="0 0 24 24" aria-hidden="true"><path d="M2 5h20v14H2z M2 5l10 8 10-8" fill="none" stroke="#2b2d30" stroke-width="2.4"/></svg>
      liam@kestreltax.com.au
    </li>
    <li class="contact__item">
      <svg class="contact__icon" viewBox="0 0 24 24" aria-hidden="true"><circle cx="12" cy="12" r="10" fill="none" stroke="#2b2d30" stroke-width="2.2"/><path d="M2 12h20M12 2c3 3 3 17 0 20M12 2c-3 3-3 17 0 20" fill="none" stroke="#2b2d30" stroke-width="1.6"/></svg>
      www.kestreltax.com.au
    </li>
  </ul>

  <div class="affiliations">
    <div class="affiliations__badge" role="img" aria-label="Professional membership badge"></div>
    <p class="affiliations__note">Kestrel Tax<br>is a member practice</p>
    <div class="affiliations__partner" role="img" aria-label="Software partner badge"></div>
  </div>
</section>

<section class="card card--back" aria-label="Card back">
  <div class="brand">
    <div class="brand__mark"></div>
    <div class="brand__name">KESTREL TAX</div>
  </div>
</section>

</body>
</html>
```